Leadership Brenvale Brochure Design*

We host a local leadership development program every two years. We need a brochure to promote the program. We would like it to be 8 1/2 x 11, tri-fold. I have attached a Word document with the necessary info for the brochure. The brochure will be professionally printed. We would like the final design to be in InDesign.

Target Market(s)

Potential participants of our leadership program. They will be local leaders, male and female, from 30-60 years of age.

Requirements
Must have
• Content as detailed in the Word document attached. Our logo.
Nice to have
• A design that is attractive to young professionals.

```html
<!DOCTYPE html>
<html lang="en">
<head>
<meta charset="utf-8">
<title>Leadership Brenvale – Tri-fold Brochure</title>
<link href="https://fonts.googleapis.com/css2?family=Montserrat:wght@400;600;700;800&family=Open+Sans:wght@400;600;700&display=swap" rel="stylesheet">
<style>
:root{
  --navy:#1d2563;
  --navy-deep:#141a4a;
  --indigo:#3a3f9e;
  --orange:#f39a1e;
  --cyan:#3fb6e4;
  --ink:#2b2f45;
  --muted:#6b6f80;
  --paper:#ffffff;
  --stage:#e7e7e9;
}
*{box-sizing:border-box;margin:0;padding:0}
html,body{width:1200px;height:2400px;overflow:hidden;background:var(--stage)}
body{position:relative;font-family:"Open Sans",Arial,sans-serif;color:var(--ink)}
.sheet{position:absolute;background:var(--paper);box-shadow:0 6px 18px rgba(0,0,0,.12);overflow:hidden}
.panel{position:absolute;top:0;width:300px;height:695px;overflow:hidden}
.photo{position:absolute}

/* brand lockup */
.brand{display:flex;align-items:center;gap:6px;font-family:"Montserrat",Arial,sans-serif;font-weight:700;font-size:11px;color:var(--navy);line-height:1.05}
.brand-dot{width:18px;height:18px;border-radius:50%;background:var(--orange);flex:none}

/* cover */
.cover{background:var(--paper)}
.cover .brand{position:absolute;left:18px;top:22px;width:110px}
.cover .photo{right:0;top:0;width:178px;height:478px;background:linear-gradient(160deg,#d9dde6 0%,#b8a593 45%,#8e7765 75%,#c9ccd6 100%)}
.cover-quote-mark{position:absolute;left:18px;top:78px;font-family:"Montserrat",Arial,sans-serif;font-weight:800;font-size:54px;line-height:1;color:var(--orange)}
.cover-quote{position:absolute;left:20px;top:120px;width:112px;font-family:"Montserrat",Arial,sans-serif;font-weight:600;font-size:12.5px;line-height:1.3;color:var(--indigo)}
.cover-band{position:absolute;left:0;top:430px;width:300px;height:265px}
.cover-sponsor{position:absolute;left:22px;top:560px;width:250px;color:#fff;font-family:"Montserrat",Arial,sans-serif}
.cover-sponsor .label{font-size:9px;font-weight:400;opacity:.85;margin-bottom:4px}
.cover-sponsor .names{font-size:12px;font-weight:700;line-height:1.35}

/* inside left */
.overview{background:var(--navy)}
.overview .photo{left:0;top:0;width:300px;height:262px;background:linear-gradient(180deg,#8f8c85 0%,#6e6a64 40%,#3f3d4b 100%)}
.overview .logo-tab{position:absolute;left:14px;top:248px;background:#fff;padding:8px 10px;border-radius:2px}
.overview .logo-tab .brand{font-size:9px;width:96px}
.overview .logo-tab .brand-dot{width:14px;height:14px}
.overview-body{position:absolute;left:22px;top:312px;width:256px;color:#fff}
.section-title{font-family:"Montserrat",Arial,sans-serif;font-weight:700;font-size:15px;margin-bottom:8px}
.overview-body p{font-size:7.6px;line-height:1.55;opacity:.92;margin-bottom:10px}
.ticks{list-style:none}
.ticks li{position:relative;padding-left:12px;font-size:7.6px;line-height:1.5;margin-bottom:6px;opacity:.92}
.ticks li::before{content:"";position:absolute;left:0;top:3px;width:5px;height:5px;border-radius:50%;background:var(--orange)}

/* schedule */
.schedule{background:var(--paper)}
.schedule-title{position:absolute;left:30px;top:40px;font-family:"Montserrat",Arial,sans-serif;font-weight:800;font-size:22px;color:var(--navy)}
.session{position:absolute;left:30px;width:245px}
.session .date{font-family:"Montserrat",Arial,sans-serif;font-weight:700;font-size:11px;color:var(--navy)}
.session .topic{font-family:"Montserrat",Arial,sans-serif;font-weight:600;font-size:9.5px;color:var(--navy);margin-top:3px;line-height:1.3}
.session .time{font-size:8px;font-weight:700;color:var(--orange);margin:4px 0 5px}
.session ul{list-style:none}
.session li{position:relative;padding-left:10px;font-size:7.4px;line-height:1.55;color:var(--muted)}
.session li::before{content:"";position:absolute;left:0;top:4px;width:4px;height:4px;background:var(--navy)}
.schedule-rule{position:absolute;left:16px;top:40px;width:3px;height:620px;background:var(--orange)}

/* outside left */
.info{background:linear-gradient(180deg,var(--navy) 0%,var(--navy-deep) 100%);color:#fff}
.info-block{position:absolute;left:26px;width:250px}
.info-block h3{display:flex;align-items:center;gap:7px;font-family:"Montserrat",Arial,sans-serif;font-weight:700;font-size:11px;color:var(--orange);margin-bottom:6px}
.info-block p{font-size:7.4px;line-height:1.55;opacity:.9}
.info-phone{position:absolute;left:0;top:575px;width:300px;text-align:center}
.info-phone p{font-size:8px;opacity:.9;line-height:1.4}
.info-phone .number{font-family:"Montserrat",Arial,sans-serif;font-weight:800;font-size:16px;color:var(--orange);margin-top:4px}

/* testimonials */
.alumni{background:var(--paper)}
.alumni-title{position:absolute;left:0;top:40px;width:300px;text-align:center;font-family:"Montserrat",Arial,sans-serif;font-weight:700;font-size:12px;color:var(--navy)}
.testimonial{position:absolute;left:30px;width:240px;text-align:center}
.testimonial .avatar{width:58px;height:58px;border-radius:50%;margin:0 auto 8px;background:radial-gradient(circle at 50% 40%,#9a9aa4,#3b3c48)}
.testimonial .name{font-family:"Montserrat",Arial,sans-serif;font-weight:700;font-size:9px;color:var(--navy)}
.testimonial .role{font-size:7.2px;color:var(--muted);margin-bottom:6px}
.testimonial p{font-size:7.2px;line-height:1.55;color:var(--muted);font-style:italic}
.alumni .brand{position:absolute;left:95px;top:630px;width:110px}
.alumni-rule{position:absolute;left:30px;top:610px;width:240px;height:2px;background:var(--orange)}
</style>
</head>
<body>

<!-- Closed front cover -->
<section class="sheet" style="left:450px;top:40px;width:300px;height:695px">
  <div class="panel cover" style="left:0">
    <div class="photo" role="img" aria-label="Photo of a smiling professional woman at a desk"></div>
    <div class="brand"><span class="brand-dot"></span>Leadership Brenvale</div>
    <div class="cover-quote-mark">“</div>
    <p class="cover-quote">The greatest wealth of a community lies not in the amount of its material, but in the quality of its leaders.</p>
    <svg class="cover-band" viewBox="0 0 300 265" aria-hidden="true">
      <polygon points="0,38 300,0 300,14 0,52" fill="var(--orange)"/>
      <polygon points="0,52 300,14 300,26 0,64" fill="var(--cyan)"/>
      <polygon points="0,64 300,26 300,265 0,265" fill="var(--navy)"/>
    </svg>
    <div class="cover-sponsor">
      <div class="label">Sponsored by:</div>
      <div class="names">Ridgeford Community College<br>Brenvale Chamber of Commerce and Tourism</div>
    </div>
  </div>
</section>

<!-- Inside spread -->
<section class="sheet" style="left:150px;top:800px;width:900px;height:695px">
  <div class="panel overview" style="left:0">
    <div class="photo" role="img" aria-label="Group photo of program participants standing in a meeting room"></div>
    <svg style="position:absolute;left:0;top:240px" width="300" height="60" aria-hidden="true">
      <polygon points="0,22 300,0 300,60 0,60" fill="var(--navy)"/>
      <polygon points="0,22 300,0 300,5 0,27" fill="var(--orange)"/>
    </svg>
    <div class="logo-tab"><div class="brand"><span class="brand-dot"></span>Leadership Brenvale</div></div>
    <div class="overview-body">
      <h2 class="section-title">Program Overview</h2>
      <p>Leadership Brenvale is a leadership development program designed to help local leaders learn more about our community. Over the course of the program, participants meet with decision makers in business, education, government and health to understand the issues shaping the region and build lasting connections.</p>
      <ul class="ticks">
        <li>Explore the strengths and challenges of our community.</li>
        <li>Build a network of leaders from many sectors and fields.</li>
        <li>Develop skills that serve local boards and civic groups.</li>
        <li>Graduates join an alumni group active across the county.</li>
      </ul>
    </div>
  </div>

  <div class="panel schedule" style="left:300px">
    <h2 class="schedule-title">Schedule:</h2>
    <div class="session" style="top:92px">
      <div class="date">January 17</div>
      <div class="topic">Organizational Retreat &amp; Dinner<br>(Attendance Mandatory)</div>
      <div class="time">9:00 a.m. – 5:00 p.m.</div>
      <ul><li>Introductions</li><li>Team Building</li><li>Leadership Styles</li><li>Program Goals</li><li>Welcome Dinner</li></ul>
    </div>
    <div class="session" style="top:300px">
      <div class="date">January 31</div>
      <div class="topic">Business &amp; Industry</div>
      <div class="time">8:30 a.m. – 4:30 p.m.</div>
      <ul><li>Manufacturing Plant Tour</li><li>Tour of Local Farm Operations</li><li>Tour of the Regional Port</li><li>Panel of Business Owners</li></ul>
    </div>
  </div>

  <div class="panel schedule" style="left:600px">
    <div class="schedule-rule"></div>
    <div class="session" style="top:40px">
      <div class="date">February 14</div>
      <div class="topic">Education</div>
      <div class="time">8:30 a.m. – 4:30 p.m.</div>
      <ul><li>Tour of the Community College</li><li>Visit with School Leaders</li><li>Early Learning Center Visit</li></ul>
    </div>
    <div class="session" style="top:200px">
      <div class="date">March 14</div>
      <div class="topic">Future Technologies &amp; Entrepreneurship</div>
      <div class="time">8:30 a.m. – 4:30 p.m.</div>
      <ul><li>Small Business Center</li><li>Startup Founders Panel</li><li>Technology Lab Tour</li></ul>
    </div>
    <div class="session" style="top:375px">
      <div class="date">April 4</div>
      <div class="topic">Government</div>
      <div class="time">8:30 a.m. – 4:30 p.m.</div>
      <ul><li>County Commission Meeting</li><li>Courthouse Tour</li><li>Public Safety Visit</li></ul>
    </div>
    <div class="session" style="top:530px">
      <div class="date">May 2</div>
      <div class="topic">Health &amp; Wellness</div>
      <div class="time">8:30 a.m. – 4:30 p.m.</div>
      <ul><li>Regional Hospital Tour</li><li>Public Health Department</li><li>Graduation Dinner</li></ul>
    </div>
  </div>
</section>

<!-- Outside spread -->
<section class="sheet" style="left:150px;top:1580px;width:900px;height:695px">
  <div class="panel info" style="left:0">
    <div class="info-block" style="top:50px">
      <h3><svg width="12" height="12" viewBox="0 0 12 12" aria-hidden="true"><path d="M2 6.5l2.5 2.5L10 3" stroke="var(--orange)" stroke-width="2" fill="none"/></svg>Attendance Policy</h3>
      <p>Participants must attend the opening retreat and may miss no more than one program day. Missed days must be made up by arrangement with staff in order to graduate.</p>
    </div>
    <div class="info-block" style="top:190px">
      <h3><svg width="12" height="12" viewBox="0 0 12 12" aria-hidden="true"><rect x="1" y="3" width="10" height="7" rx="1" stroke="var(--orange)" stroke-width="1.5" fill="none"/></svg>Tuition</h3>
      <p>Tuition covers all program days, meals, tours and materials. Employers often sponsor participants, and a limited number of scholarships are available on request.</p>
    </div>
    <div class="info-block" style="top:330px">
      <h3><svg width="12" height="12" viewBox="0 0 12 12" aria-hidden="true"><circle cx="6" cy="6" r="4.5" stroke="var(--orange)" stroke-width="1.5" fill="none"/></svg>Eligibility</h3>
      <p>Applicants should live or work in the county and show a commitment to community service. Classes are selected to reflect a mix of sectors, ages and backgrounds.</p>
    </div>
    <div class="info-phone">
      <svg width="22" height="22" viewBox="0 0 24 24" aria-hidden="true"><path d="M6.6 10.8a15 15 0 006.6 6.6l2.2-2.2a1 1 0 011-.25 11.4 11.4 0 003.6.57 1 1 0 011 1V20a1 1 0 01-1 1A17 17 0 013 4a1 1 0 011-1h3.5a1 1 0 011 1c0 1.25.2 2.45.57 3.6a1 1 0 01-.25 1z" fill="var(--orange)"/></svg>
      <p>For questions, please call<br>Leadership Brenvale at</p>
      <div class="number">555-014-2277</div>
    </div>
  </div>

  <div class="panel alumni" style="left:300px">
    <h2 class="alumni-title">What Community Alumni are Saying</h2>
    <div class="testimonial" style="top:85px">
      <div class="avatar" role="img" aria-label="Portrait of a program graduate"></div>
      <div class="name">Dana Whitfield</div>
      <div class="role">Class of 2019, Bank Branch Manager</div>
      <p>“The program opened doors I never knew existed. I met leaders from every corner of the county and came away with a clearer picture of how our community works and where I can help.”</p>
    </div>
    <div class="testimonial" style="top:345px">
      <div class="avatar" role="img" aria-label="Portrait of a program graduate"></div>
      <div class="name">Marcus Hale</div>
      <div class="role">Class of 2021, School Principal</div>
      <p>“Every session gave me something to bring back to my staff. The friendships formed in this class continue today, and we still work together on projects across town.”</p>
    </div>
    <div class="alumni-rule"></div>
    <div class="brand"><span class="brand-dot"></span>Leadership Brenvale</div>
  </div>

  <div class="panel cover" style="left:600px">
    <div class="photo" role="img" aria-label="Photo of a smiling professional woman at a desk"></div>
    <div class="brand"><span class="brand-dot"></span>Leadership Brenvale</div>
    <div class="cover-quote-mark">“</div>
    <p class="cover-quote">The greatest wealth of a community lies not in the amount of its material, but in the quality of its leaders.</p>
    <svg class="cover-band" viewBox="0 0 300 265" aria-hidden="true">
      <polygon points="0,38 300,0 300,14 0,52" fill="var(--orange)"/>
      <polygon points="0,52 300,14 300,26 0,64" fill="var(--cyan)"/>
      <polygon points="0,64 300,26 300,265 0,265" fill="var(--navy)"/>
    </svg>
    <div class="cover-sponsor">
      <div class="label">Sponsored by:</div>
      <div class="names">Ridgeford Community College<br>Brenvale Chamber of Commerce and Tourism</div>
    </div>
  </div>
</section>

</body>
</html>
```